Local new marketing agency (croatia) need ad design for billboard advertisement dimensions 5x2.4

We are a new company and we are looking for new clients for our led display billboards. We want a slightly provocative with allusion on different things , slightly comical or funny advertisement that will encourage business owners to think that this particular location and our billboard is the right place for them to place their advertisement.It is not mandatory that the advertisement has to be funny.This advertisemet will be on all our locations.Name of company , TALVEX MEDIA . HR

```html
<!DOCTYPE html>
<html lang="hr">
<head>
<meta charset="utf-8">
<title>Talvex Media – Get Space billboard</title>
<link href="https://fonts.googleapis.com/css2?family=League+Spartan:wght@700&family=Josefin+Sans:wght@400;600&display=swap" rel="stylesheet">
<style>
  :root {
    --page: #ffffff;
    --space-top: #0b1233;
    --space-mid: #141a45;
    --space-low: #3a1a2a;
    --space-glow: #8a2a1c;
    --white: #ffffff;
    --red: #ee2b38;
    --suit-light: #d9d6e6;
    --suit-shade: #6f6a8e;
  }
  * { margin: 0; padding: 0; box-sizing: border-box; }
  html, body {
    width: 877px; height: 1200px; overflow: hidden;
    background: var(--page);
  }
  .canvas { position: relative; width: 877px; height: 1200px; }
  .billboard {
    position: absolute; left: 28px; top: 403px;
    width: 820px; height: 394px; overflow: hidden;
    background:
      radial-gradient(ellipse 60% 45% at 50% 108%, var(--space-glow) 0%, transparent 70%),
      linear-gradient(180deg, var(--space-top) 0%, var(--space-mid) 55%, var(--space-low) 100%);
    box-shadow: 8px 10px 14px rgba(0,0,0,0.35);
  }
  .astronaut-photo {
    position: absolute; left: 50px; top: 18px;
    width: 330px; height: 357px;
    border-radius: 46% 50% 44% 52%;
    background: radial-gradient(ellipse at 55% 40%, var(--suit-light) 0%, var(--suit-shade) 60%, transparent 78%);
  }
  .agency-name {
    position: absolute; left: 357px; top: 44px;
    font-family: "Josefin Sans", sans-serif; font-weight: 400;
    font-size: 19px; letter-spacing: 0.42em; color: var(--white);
    white-space: nowrap;
  }
  .headline {
    position: absolute; left: 352px;
    font-family: "League Spartan", sans-serif; font-weight: 700;
    font-size: 128px; line-height: 1; letter-spacing: -0.01em;
    white-space: nowrap;
  }
  .headline--get { top: 91px; color: var(--white); }
  .headline--space { top: 199px; color: var(--red); }
  .phone {
    position: absolute; left: 354px; top: 322px;
    font-family: "Josefin Sans", sans-serif; font-weight: 600;
    font-size: 46px; line-height: 1; color: var(--white);
    white-space: nowrap;
  }
</style>
</head>
<body>
  <main class="canvas">
    <section class="billboard">
      <div class="astronaut-photo" role="img" aria-label="Photo of an astronaut in a white spacesuit floating in space"></div>
      <p class="agency-name">TALVEX MEDIA . HR</p>
      <h1>
        <span class="headline headline--get">GET</span>
        <span class="headline headline--space">SPACE</span>
      </h1>
      <p class="phone">385 4100 2290</p>
    </section>
  </main>
</body>
</html>
```